Kestrel Plumbing business card full re design & logo design

Kestrel Plumbing is a Sydney based mechanical plumbing contractor company.
We would like a full redesign with new logo etc which we can take to a future website, uniforms, vehicle sign writing etc.
Blue is my preferred choice of colour but i would be open to see a couple of alternatives thrown in the mix to see how they compare. I am open to see on white cards, black cards etc. Open to many new ideas.
Please see attached original business cards which have been used for the last 5 years.

Target Market(s)

Mechanical services industry.

Industry/Entity Type

Plumbing

Contact Information for Business Card

Dale Fenmore
Director

Mob: 0427 596 418
Email: dale@kestrelplumbing-demo.net.au
PO BOX 782
Tarrowby NSW 2163
Lic: 518604k

Logo Text

Kestrel Plumbing

Font styles to use
Sans Serif

Colors
0655a3
3276b5
0792cd
33a6d7
85cae6
000000
333333
474747

Requirements
Must have
• Things that make it very professional and very well presented.
Nice to have
• Same description or very similar to attached uploaded file
Should not have
• Anything that makes it look unprofessional or cartoony.

```html
<!DOCTYPE html>
<html lang="en">
<head>
<meta charset="utf-8">
<title>Kestrel Plumbing – Business Card</title>
<link href="https://fonts.googleapis.com/css2?family=Source+Sans+3:wght@400;600;700&family=Nunito+Sans:wght@300;400&display=swap" rel="stylesheet">
<style>
  :root {
    --stage: #7a7a7a;
    --white: #ffffff;
    --charcoal: #3f3f3f;
    --slate: #545856;
    --pipe: #5a5f5c;
    --sky: #85c0d6;
    --brand-blue: #2f4e95;
    --ink: #222222;
    --faint: #575757;
    --body-font: "Source Sans 3", "Myriad Pro", Arial, sans-serif;
    --light-font: "Nunito Sans", "Avenir", Arial, sans-serif;
  }
  * { margin: 0; padding: 0; box-sizing: border-box; }
  html, body { width: 1200px; height: 1200px; overflow: hidden; }
  body { background: var(--stage); position: relative; font-family: var(--body-font); }

  .card {
    position: absolute;
    transform: scale(0.8);
    transform-origin: top left;
    overflow: hidden;
  }
  .card svg.card-shapes { position: absolute; inset: 0; }
  .card-front { left: 269px; top: 148px; width: 828px; height: 473px; background: var(--white); }
  .card-back { left: 268px; top: 672px; width: 831px; height: 475px; background: var(--charcoal); }

  .abs { position: absolute; white-space: nowrap; }
  .right { text-align: right; right: 42px; }

  /* Front */
  .person-name { top: 96px; font-size: 38px; color: var(--ink); font-weight: 400; line-height: 1; }
  .person-name .surname { color: var(--brand-blue); }
  .person-role { top: 137px; font-size: 27px; color: var(--sky); line-height: 1; }
  .contact { top: 225px; color: var(--white); font-size: 24px; line-height: 28px; letter-spacing: .3px; }
  .contact .label { color: var(--sky); font-size: 16px; }
  .contact .email { font-size: 17px; line-height: 34px; }
  .services-line { top: 385px; right: 42px; color: var(--white); font-family: var(--light-font); font-size: 20px; letter-spacing: .3px; }
  .website { top: 431px; right: 42px; color: var(--ink); font-size: 20px; }

  .brand-lockup { display: flex; align-items: center; gap: 12px; }
  .brand-lockup .brand-mark { width: 26px; height: 26px; flex: none; }
  .brand-lockup .brand-name { font-family: var(--body-font); font-weight: 700; font-size: 30px; line-height: 32px; letter-spacing: .5px; }
  .front-brand { left: 50px; top: 308px; }
  .front-brand .brand-mark { background: var(--brand-blue); }
  .front-brand .brand-name { color: var(--brand-blue); }

  /* Back */
  .back-title { left: 263px; top: 68px; color: var(--white); font-family: var(--light-font); font-weight: 300; font-size: 31px; }
  .back-subtitle { left: 265px; top: 110px; color: var(--white); font-family: var(--light-font); font-weight: 300; font-size: 19px; }
  .specialties { top: 196px; right: 65px; list-style: none; text-align: right; color: var(--white); font-family: var(--light-font); font-weight: 300; font-size: 15px; line-height: 24.4px; }
  .tagline { top: 376px; right: 65px; color: var(--white); font-family: var(--light-font); font-weight: 300; font-size: 21px; }
  .back-brand { left: 58px; top: 362px; }
  .back-brand .brand-mark { background: var(--faint); }
  .back-brand .brand-name { color: var(--faint); }
</style>
</head>
<body>

<section class="card card-front" aria-label="Business card front">
  <svg class="card-shapes" width="828" height="473" viewBox="0 0 828 473" aria-hidden="true">
    <polygon points="0,0 584,0 553,37 0,37" fill="var(--charcoal)"/>
    <polygon points="584,0 635,0 604,37 553,37" fill="var(--sky)"/>
    <path d="M450,198 Q458,187 470,187 L828,187 L828,211 L436,211 Z" fill="var(--charcoal)"/>
    <polygon points="484,211 828,211 828,372 345,372" fill="var(--slate)"/>
    <polygon points="436,211 484,211 345,372 295,372" fill="var(--sky)"/>
    <path d="M295,372 L828,372 L828,423 L0,423 L0,393 L270,393 Q282,393 295,372 Z" fill="var(--charcoal)"/>
  </svg>

  <div class="abs front-brand brand-lockup">
    <span class="brand-mark"></span>
    <span class="brand-name">KESTREL<br>PLUMBING</span>
  </div>

  <p class="abs right person-name">Dale <span class="surname">Fenmore</span></p>
  <p class="abs right person-role">Director</p>

  <div class="abs right contact">
    <p><span class="label">MOB:</span> 0427 596 418</p>
    <p>PO Box 782</p>
    <p>Tarrowby NSW 2163</p>
    <p><span class="label">LIC:</span> 518604k</p>
    <p class="email"><span class="label">EMAIL:</span> dale@kestrelplumbing-demo.net.au</p>
  </div>

  <p class="abs services-line">MECHANICAL PIPING | CHW | HW | CW | REFRIG</p>
  <p class="abs website">www.kestrelplumbing-demo.net.au</p>
</section>

<section class="card card-back" aria-label="Business card back">
  <svg class="card-shapes" width="831" height="475" viewBox="0 0 831 475" aria-hidden="true">
    <rect x="0" y="72" width="200" height="58" fill="var(--pipe)"/>
    <rect x="200" y="66" width="26" height="68" fill="var(--pipe)"/>
    <rect x="296" y="362" width="535" height="59" fill="var(--pipe)"/>
    <rect x="270" y="358" width="26" height="67" fill="var(--pipe)"/>
  </svg>

  <h2 class="abs back-title">MECHANICAL PLUMBING SERVICES</h2>
  <p class="abs back-subtitle">SPECIALASING IN:</p>

  <ul class="abs specialties">
    <li>MAKE GOOD</li>
    <li>REFURBISHMENT</li>
    <li>TENANCY FIT OUT</li>
    <li>PLANT ROOM WORKS</li>
    <li>SHUT DOWNS</li>
    <li>CHANGE OWERS</li>
  </ul>

  <div class="abs back-brand brand-lockup">
    <span class="brand-mark"></span>
    <span class="brand-name">KESTREL<br>PLUMBING</span>
  </div>

  <p class="abs tagline">KESTREL have the SOLUTION</p>
</section>

</body>
</html>
```